Newsletter Design Project

We are looking at refreshing our corporate newsletter and general communication design.
The design will be a corporate design for our brand:
VRIL - Northern Journey Planners Guild
For brand colours, requirements and logo look here: www.vrilguild-example.org/media
or check the attached documents.

We need to incorporate logo and brand but we are happy to refresh the palette.

Important! Attached please also find designs and colour palette of our new website-newsletter should complement these.

You are also free to use photos from events some of which can be found here:
http://www.examplebook.test/pages/Northern-Journey-Planners-Guild/904517263380419?sk=photos_stream

We attached a sample of our newsletter. We usually include sections such as:
-CONTENTS (for navigation)
-INTRODUCTION
-NEW MEMBERS
-EVENTS
-FEATURES
-IN THE MEDIA
-ABOUT VRIL

Most important:
-PROFESSIONAL AUDIENCE-PROFESSIONAL DESIGN
-SIMPLE (see example our homepage in attachment)
-IMAGES AND GRAPHS OK
-DESIGN TO BE RE-USABLE FOR OTHER COMMUNICATIONS
-HTML format please
Updates

We are happy to increase the budget if the design is right

We have uploaded new social media icons which we would like integrated in  the design

I have uploaded a new high res version of the map that you can integrate in your designs (feel free to change colour scheme if needed)

I have also posted another Chirpnet + corporate social media icon (as some mentioned it wasn't working)

Target Market(s)

B2B- audience includes various tourism companies

Industry/Entity Type

Communication

```html
<!DOCTYPE html>
<html lang="en">
<head>
<meta charset="utf-8">
<title>VRIL Newsletter</title>
<link href="https://fonts.googleapis.com/css2?family=Open+Sans:wght@400;600;700&display=swap" rel="stylesheet">
<style>
:root{
  --navy:#0f1a45;
  --navy-deep:#0a1236;
  --header-light:#3f63a8;
  --accent:#5b84c4;
  --link:#4a76bd;
  --panel:#ececec;
  --panel-blue:#e6ebf3;
  --rule:#9db3da;
  --text:#3a3a3a;
  --heading:#111a3a;
  --ring:#8c8c8c;
  --ring-fill:#e2e2e2;
  --white:#ffffff;
}
*{margin:0;padding:0;box-sizing:border-box}
html,body{width:1200px;height:2400px;overflow:hidden}
body{position:relative;background:var(--white);font-family:"Open Sans",Arial,sans-serif;color:var(--text)}
.abs{position:absolute}
.masthead{left:0;top:0;width:1200px;height:312px;background:radial-gradient(ellipse 700px 320px at 560px 60px,var(--header-light),var(--navy) 75%)}
.social{display:flex;gap:6px}
.social-item{height:40px;padding:0 6px;background:var(--navy-deep);color:var(--white);font-size:10px;font-weight:600;display:flex;align-items:center;justify-content:center;border:2px solid var(--white)}
.masthead-title{left:66px;top:140px;font-size:110px;font-weight:400;color:var(--white);letter-spacing:-4px;line-height:1}
.issue-date{left:490px;top:258px;font-size:15px;font-weight:700;color:var(--white)}
.ribbon{left:880px;top:0}
.brand{left:926px;top:22px;width:154px;height:150px;display:flex;align-items:center;justify-content:center;gap:10px;color:var(--white);font-size:28px;font-weight:400}
.brand-dot{width:14px;height:14px;border-radius:50%;background:var(--white)}
.contents{left:886px;top:312px;width:242px;list-style:none}
.contents li{height:45px;display:flex;align-items:center;justify-content:space-between;padding:0 36px 0 34px;color:var(--white);font-size:15px;border-bottom:1px solid #3c5a94}
.photo{display:block}
.panel{left:72px;width:784px;background:var(--panel);border-bottom:2px solid var(--rule)}
.section-label{font-size:24px;font-weight:700;color:var(--heading);line-height:1.2}
.article-title{font-size:22px;font-weight:700;color:var(--link);line-height:1.2;margin-bottom:2px}
.article-body{font-size:15.5px;line-height:22px;text-align:justify}
.read-more{font-size:13px;font-weight:600;color:var(--link);text-align:right;margin-top:14px}
.sidebar-heading{left:884px;width:316px;background:var(--accent);color:var(--white);font-size:28px;font-weight:600;padding-left:24px;display:flex;align-items:center;letter-spacing:-0.5px}
.member-logo{width:140px;height:140px;border-radius:50%;border:11px solid var(--ring);background:var(--ring-fill);display:flex;align-items:center;justify-content:center;font-size:11px;color:var(--link);left:966px}
.events{left:896px;top:2018px;list-style:none}
.events li{margin-bottom:22px}
.event-title{font-size:21px;font-weight:700;color:var(--link);line-height:1.1}
.event-date{font-size:15px;color:var(--text)}
.about{left:72px;top:2164px;width:784px;height:106px;background:linear-gradient(90deg,var(--navy-deep),var(--navy) 55%,#4a6fb3);color:var(--white);padding:12px 32px;box-shadow:0 6px 10px rgba(0,0,0,.35)}
.about h2{font-size:21px;font-weight:700;line-height:1.1}
.about p{font-size:13px;line-height:17px}
.about .legal{margin-top:10px;font-size:13px}
.footer-copy{left:72px;top:2334px;font-size:13px;color:var(--heading)}
.footer-follow{left:790px;top:2334px;font-size:13px;font-weight:600;color:var(--heading)}
</style>
</head>
<body>

<header class="abs masthead"></header>
<nav class="abs social" style="left:72px;top:0">
  <span class="social-item">Examplebook</span>
  <span class="social-item">Chirpnet</span>
  <span class="social-item">Clipstream</span>
  <span class="social-item">Workweb</span>
</nav>
<h1 class="abs masthead-title">Newsletter</h1>
<div class="abs issue-date">05 | MARCH</div>

<svg class="abs ribbon" width="260" height="720" viewBox="0 0 260 720" aria-hidden="true">
  <polygon points="10,6 252,6 252,660 10,700" fill="rgba(0,0,0,.25)"/>
  <polygon points="6,0 248,0 248,650 6,690" fill="var(--navy)"/>
  <line x1="6" y1="312" x2="248" y2="312" stroke="#2b3d75" stroke-width="2"/>
</svg>
<div class="abs brand"><span class="brand-dot"></span>VRIL</div>
<ul class="abs contents">
  <li>SECTION A<span>›</span></li>
  <li>SECTION B<span>›</span></li>
  <li>SECTION C<span>›</span></li>
  <li>SECTION D<span>›</span></li>
  <li>SECTION E<span>›</span></li>
  <li>EVENTS<span>›</span></li>
</ul>

<div class="abs photo" role="img" aria-label="Photo of a busy conference hall with delegates meeting at tables" style="left:72px;top:312px;width:784px;height:268px;background:linear-gradient(180deg,#b9a27a,#6d5a46 55%,#3a3236)"></div>

<section class="abs panel" style="top:580px;height:290px;padding:50px 12px 0 12px">
  <h2 class="section-label">SECTION A</h2>
  <h3 class="article-title">ArticleTitle</h3>
  <p class="article-body">Lorem ipsum dolor sit amet, consectetuer adipiscing elit. Duis pulvinar lectus. Fusce lacinia. Cras massa tortor, dignissim eu, sollicitudin eu, consequat et, magna. Proin tempor. Mauris leo orci, pretium at, pharetra a, egestas id, ligula. Morbi non magna. Nunc auctor nibh ac justo. Quisque egestas imperdiet risus. Nunc nibh ligula, imperdiet non, feugiat eu, commodo quis, justo. In hac habitasse platea dictumst. Aliquam in enim. Donec dignissim metus ac purus. Aliquam sed mi non diam molestie posuere. Lorem ipsum dolor sit amet, consectetuer adipiscing elit. Fusce velit. Phasellus cursus.</p>
  <p class="read-more">| READ MORE</p>
</section>

<section class="abs panel" style="top:880px;height:270px;padding:22px 12px 0 342px">
  <h2 class="section-label">SECTION B</h2>
  <h3 class="article-title">ArticleTitle</h3>
  <p class="article-body">Lorem ipsum dolor sit amet, consectetuer adipiscing elit. Quisque egestas imperdiet risus. Nunc nibh ligula, imperdiet non, feugiat eu, commodo quis, justo. In hac habitasse platea dictumst. Aliquam in enim. Donec dignissim metus ac purus. Aliquam sed mi non diam molestie posuere. Lorem ipsum dolor sit amet, consectetuer adipiscing elit. Fusce velit. Phasellus cursus.</p>
</section>
<div class="abs photo" role="img" aria-label="Photo of a large exhibition hall filled with meeting tables" style="left:72px;top:904px;width:326px;height:208px;background:linear-gradient(160deg,#c7a36a,#7a5a3c 50%,#2e3550)"></div>

<section class="abs panel" style="top:1150px;height:340px;padding:30px 400px 0 12px">
  <h2 class="section-label">SECTION C</h2>
  <h3 class="article-title">ArticleTitle</h3>
  <p class="article-body">Lorem ipsum dolor sit amet, consectetuer adipiscing elit. Duis pulvinar lectus. Fusce lacinia. Cras massa tortor, dignissim eu, sollicitudin eu, consequat et, magna. Proin tempor. Mauris leo orci, pretium at, pharetra a, egestas id, ligula. Morbi non magna. Nunc auctor nibh ac justo. Quisque egestas imperdiet risus. Nunc nibh ligula, imperdiet non, feugiat eu, commodo quis, justo. In hac habitasse platea dictumst.</p>
  <p class="read-more">| READ MORE</p>
</section>
<div class="abs photo" role="img" aria-label="Photo of two delegates talking at a conference table" style="left:504px;top:1188px;width:352px;height:280px;background:linear-gradient(150deg,#8f8a86,#4a4042 50%,#1f2644)"></div>

<section class="abs panel" style="top:1490px;height:382px;padding:34px 400px 0 12px">
  <h2 class="section-label">SECTION D</h2>
  <h3 class="article-title">ArticleTitle</h3>
  <p class="article-body">Lorem ipsum dolor sit amet, consectetuer adipiscing elit. Duis pulvinar lectus. Fusce lacinia. Cras massa tortor, dignissim eu, sollicitudin eu, consequat et, magna. Proin tempor. Mauris leo orci, pretium at, pharetra a, egestas id, ligula. Morbi non magna. Nunc auctor nibh ac justo.<br>Aliquam in enim. Donec dignissim metus ac purus. Aliquam sed mi non diam molestie posuere. Lorem ipsum dolor sit amet, consectetuer adipiscing elit. Fusce velit. Phasellus cursus.</p>
  <p class="read-more">| READ MORE</p>
</section>
<div class="abs photo" role="img" aria-label="Photo of a meeting room with tall windows at dusk and delegates at tables" style="left:504px;top:1524px;width:352px;height:312px;background:linear-gradient(180deg,#a9b6c9,#d7a46a 40%,#3a3040 75%,#1c2240)"></div>

<svg class="abs" style="left:72px;top:1882px" width="1128" height="4" aria-hidden="true"><line x1="0" y1="2" x2="1128" y2="2" stroke="var(--rule)" stroke-width="2"/></svg>

<section class="abs panel" style="top:1900px;height:240px;padding:28px 12px 0 342px;background:var(--panel-blue);border-bottom:none">
  <h2 class="section-label">SECTION E</h2>
  <h3 class="article-title">ArticleTitle</h3>
  <p class="article-body">Nunc auctor nibh ac justo. Quisque egestas imperdiet risus. Nunc nibh ligula, imperdiet non, commodo quis, justo. In hac habitasse platea dictumst. Lorem ipsum dolor sit amet, consectetuer adipiscing elit. Fusce velit. Phasellus cursus.</p>
  <p class="read-more">| READ MORE</p>
</section>
<div class="abs photo" role="img" aria-label="Photo of delegates seated at a networking event" style="left:72px;top:1922px;width:326px;height:190px;background:linear-gradient(150deg,#8a8fa6,#5a4c4c 50%,#2a3150)"></div>

<aside>
  <h2 class="abs sidebar-heading" style="top:734px;height:88px">NEW MEMBERS</h2>
  <div class="abs member-logo" style="top:904px">LOGO</div>
  <div class="abs member-logo" style="top:1078px">LOGO</div>
  <div class="abs member-logo" style="top:1250px">LOGO</div>
  <div class="abs member-logo" style="top:1424px">LOGO</div>
  <div class="abs member-logo" style="top:1598px">LOGO</div>

  <h2 class="abs sidebar-heading" style="top:1900px;height:86px">EVENTS</h2>
  <ul class="abs events">
    <li><div class="event-title">› Title</div><div class="event-date">Year | Month | Day</div></li>
    <li><div class="event-title">› Title</div><div class="event-date">Year | Month | Day</div></li>
    <li><div class="event-title">› Title</div><div class="event-date">Year | Month | Day</div></li>
    <li><div class="event-title">› Title</div><div class="event-date">Year | Month | Day</div></li>
  </ul>
  <div class="abs read-more" style="left:1000px;top:2280px;width:120px;margin:0">| FIND MORE</div>
  <svg class="abs" style="left:884px;top:2324px" width="316" height="4" aria-hidden="true"><line x1="0" y1="2" x2="316" y2="2" stroke="var(--rule)" stroke-width="2"/></svg>
</aside>

<footer>
  <div class="abs about">
    <h2>ABOUT VRIL</h2>
    <p>VRIL was formed to give Europe’s inbound industry a political voice. Since 1989, VRIL has represented its members in the European political arena, delivering specialist seminars and hosting major workshops.</p>
    <p class="legal"><b>VRIL Ltd.</b> |14 Quarry Lane, Northby NB2 7QX | UK | <b>REGISTRATION NUMBER</b> 8312604</p>
  </div>
  <div class="abs footer-copy"><b>COPYRIGHT © 2013</b> | All rights reserved</div>
  <div class="abs footer-follow">Follow us</div>
  <div class="abs social" style="left:560px;top:2356px">
    <span class="social-item">Examplebook</span>
    <span class="social-item">Chirpnet</span>
    <span class="social-item">Clipstream</span>
    <span class="social-item">Workweb</span>
  </div>
</footer>

</body>
</html>
```